CD/Album cover design - Ember & Tide

Hi, I need an album cover designed. The name of the album is called 'Ember and Tide' Not 100% sure of the concept, but using colored lines, Geometrical shapes etc, angles and maybe a circle or triangle in the middle. A cross between, Velvet Harbor ,Paper towns of the rain (But dont make it look like this old look album) , 80s retro synthwave album covers, perhaps with neon color lines but not all of it etc. Have it modern looking . My name on cover and album name. Back, songs etc and info details. The style of the music is EDM meets guitar. Trap, house music and guitar as the main theme instrument, with sythns. Keep it relatively simple looking, and maybe have the background white,, but with the color designs, wording etc colors. or if you feel it would look better another way, just use your own judgement and creativity. Ve attached a couple of Pics. The Velvet Hrabor pic , more of concept. The retro one... I like the design in the middle but not wording at the top. The QJ crest one, I like how the wording is in the middle of circle. So a combination of these, with geometrical lines, colors, etc. I am also open to a completely new idea that you think would look awesome. The album is really combining Guitar with House/Tap EDM music, and the concept Ember and Tide - The beginning and end (Of everything) Thanks
Target Market(s)
EDM , Guitarists
Industry/Entity Type
Music, EDM, Guitar Instrumental
Look and feel

```html
<!DOCTYPE html>
<html lang="en">
<head>
<meta charset="utf-8">
<title>Ember and Tide — Album Cover</title>
<link rel="stylesheet" href="https://fonts.googleapis.com/css2?family=Montserrat:wght@300&display=swap">
<style>
  :root {
    --sky-top: #07121a;
    --sky-mid: #0d3640;
    --sky-low: #6b747a;
    --sky-haze: #a08878;
    --sky-ember: #c85a2a;
    --band-top: #0f2d48;
    --band-mid: #1a8aaa;
    --band-low: #a6c2cb;
    --band-haze: #cbbcaa;
    --band-ember: #d88a50;
    --cloud-orange: #f26a2e;
    --cloud-peach: #f4a08a;
    --cloud-violet: #8a86c8;
    --cloud-blue: #3a55b0;
    --title-light: #ffffff;
    --title-dark: #0e0f3e;
  }
  * { margin: 0; padding: 0; box-sizing: border-box; }
  html, body {
    width: 1200px;
    height: 1200px;
    overflow: hidden;
    background: var(--sky-top);
  }
  .cover {
    position: relative;
    width: 1200px;
    height: 1200px;
    overflow: hidden;
  }
  .cover-art {
    position: absolute;
    inset: 0;
    display: block;
  }
  .album-title {
    position: absolute;
    left: 0;
    right: 0;
    top: 532px;
    text-align: center;
    font-family: "Montserrat", sans-serif;
    font-weight: 300;
    font-size: 68px;
    line-height: 1;
    letter-spacing: 0.49em;
    padding-left: 0.49em;
    color: var(--title-light);
    white-space: nowrap;
  }
  .album-title .title-link {
    color: var(--title-dark);
  }
</style>
</head>
<body>
  <main class="cover">
    <svg class="cover-art" width="1200" height="1200" viewBox="0 0 1200 1200" xmlns="http://www.w3.org/2000/svg">
      <defs>
        <linearGradient id="sky-gradient" x1="0" y1="0" x2="0" y2="1">
          <stop offset="0" stop-color="var(--sky-top)"/>
          <stop offset="0.45" stop-color="var(--sky-mid)"/>
          <stop offset="0.7" stop-color="var(--sky-low)"/>
          <stop offset="0.86" stop-color="var(--sky-haze)"/>
          <stop offset="1" stop-color="var(--sky-ember)"/>
        </linearGradient>
        <linearGradient id="band-gradient" x1="0" y1="0" x2="0" y2="1">
          <stop offset="0" stop-color="var(--band-top)"/>
          <stop offset="0.45" stop-color="var(--band-mid)"/>
          <stop offset="0.72" stop-color="var(--band-low)"/>
          <stop offset="0.88" stop-color="var(--band-haze)"/>
          <stop offset="1" stop-color="var(--band-ember)"/>
        </linearGradient>
        <linearGradient id="cloud-gradient" x1="0.2" y1="0" x2="0.6" y2="1">
          <stop offset="0" stop-color="var(--cloud-orange)"/>
          <stop offset="0.35" stop-color="var(--cloud-peach)"/>
          <stop offset="0.55" stop-color="var(--cloud-violet)"/>
          <stop offset="0.72" stop-color="var(--cloud-peach)"/>
          <stop offset="1" stop-color="var(--cloud-blue)"/>
        </linearGradient>
        <clipPath id="triangle-clip">
          <polygon points="127,135 1073,135 600,1081"/>
        </clipPath>
      </defs>

      <g class="sky-backdrop" role="img" aria-label="Night sky with stars fading into a sunset horizon">
        <rect width="1200" height="1200" fill="url(#sky-gradient)"/>
      </g>

      <g class="sky-bands" role="img" aria-label="Vertical bands of brighter blue sky fading into sunset">
        <rect x="165" y="0" width="174" height="1200" fill="url(#band-gradient)"/>
        <rect x="513" y="0" width="174" height="1200" fill="url(#band-gradient)"/>
        <rect x="861" y="0" width="174" height="1200" fill="url(#band-gradient)"/>
      </g>

      <g class="cloud-triangle" role="img" aria-label="Inverted triangle filled with orange and pink sunset clouds over blue sky">
        <polygon points="127,135 1073,135 600,1081" fill="url(#cloud-gradient)"/>
        <g clip-path="url(#triangle-clip)" fill="#ffffff" opacity="0.08">
          <rect x="165" y="0" width="174" height="1200"/>
          <rect x="513" y="0" width="174" height="1200"/>
          <rect x="861" y="0" width="174" height="1200"/>
        </g>
      </g>
    </svg>

    <h1 class="album-title">EMBER <span class="title-link">AND</span> TIDE</h1>
  </main>
</body>
</html>
```